lantern-folk - the complementary consultancy

Please create a powerpoint template for us. We are a management consultancy that combines the business aspects with the values and culture-oriented aspects (= we are a complementary consultancy).

Please also take into account the following key data:
- Logo see appendix
- Colors in the logo see appendix

I need a quick fix :))

----------------
We are a consulting company that offers its customers complementary advice for mission-critical transformation projects.

Complementary counseling integrates different perspectives and approaches to offer more comprehensive solutions and better understanding. By combining methods, models and theories from different disciplines, she supports individual needs and goals of clients or organizations.

The core idea is that connecting different approaches leads to a more comprehensive understanding and more effective solutions. It develops bespoke solutions tailored to specific needs and contexts, rather than being limited to a single theory or method.

Target Market(s)

Top management of VEK companies

Font styles to use
Other font styles liked:
• Roboto

Requirements
Must have
• PPT template including cover page, table of contents, content page, back page
Should not have
• no new logo

```html
<!DOCTYPE html>
<html lang="en">
<head>
<meta charset="utf-8">
<title>Lantern-Folk – Presentation Template</title>
<link href="https://fonts.googleapis.com/css2?family=Roboto:wght@300;400;500;700&display=swap" rel="stylesheet">
<style>
:root{
  --brand-blue:#0b67ae;
  --brand-blue-deep:#0a5a9c;
  --accent-blue:#1a9ad6;
  --arc-grey:#a9a9a9;
  --table-grey:#7d7d7d;
  --text-dark:#333;
  --text-mid:#555;
  --rule:#e3e3e3;
  --canvas:#dcdcdc;
  --white:#fff;
}
*{margin:0;padding:0;box-sizing:border-box}
html,body{width:1200px;height:2424px;overflow:hidden}
body{background:var(--canvas);font-family:"Roboto",sans-serif;color:var(--text-dark);position:relative}

.slide{position:absolute;width:540px;height:303px;overflow:hidden;background:var(--white)}
.slide--hero{left:226px;top:107px;transform:scale(1.3889);transform-origin:0 0}
.pos-a{left:51px}.pos-b{left:609px}
.row-1{top:788px}.row-2{top:1109px}.row-3{top:1431px}.row-4{top:1752px}
.slide--back{left:330px;top:2074px}

.arcs{position:absolute;inset:0;width:540px;height:303px}

/* cover */
.cover__photo{position:absolute;inset:0;background:linear-gradient(180deg,#b9c3e0 0%,#8a88ab 30%,#4f5679 47%,#23426f 62%,#0d2b56 100%)}
.cover__photo--night{background:linear-gradient(180deg,#7d93b8 0%,#4f6f9c 35%,#2a5688 55%,#143f73 100%)}
.cover__fade{position:absolute;inset:0;background:linear-gradient(90deg,rgba(244,246,250,.98) 0%,rgba(240,243,250,.9) 30%,rgba(235,240,250,.25) 58%,rgba(235,240,250,0) 70%)}
.cover__fade--blue{background:linear-gradient(90deg,#0d6ab2 0%,#0f6cb4 38%,rgba(15,108,180,.55) 55%,rgba(15,108,180,0) 70%)}
.cover__content{position:absolute;left:35px;top:0;width:260px;height:303px}
.brand{position:absolute;display:flex;align-items:center;gap:5px;font-weight:500;letter-spacing:.14em;color:var(--brand-blue);white-space:nowrap}
.brand__dot{width:7px;height:7px;border-radius:50%;background:currentColor}
.cover .brand{left:0;top:62px;font-size:11px}
.cover__title{position:absolute;left:0;top:116px;font-size:26px;line-height:27px;font-weight:700;color:var(--brand-blue);letter-spacing:-.2px}
.cover__lead{position:absolute;left:0;top:178px;font-size:7.3px;line-height:8.5px;color:var(--text-mid)}
.cover__date{position:absolute;left:0;top:228px;font-size:6.2px;color:var(--text-mid)}
.cover__copy{position:absolute;left:0;top:264px;font-size:5.6px;color:#777}
.cover--blue{background:#0f6cb4}
.cover--blue .brand,.cover--blue .cover__title,.cover--blue .cover__lead,.cover--blue .cover__date,.cover--blue .cover__copy{color:var(--white)}

/* content slides */
.content__heading{position:absolute;left:36px;top:20px;font-size:20px;font-weight:500;color:var(--brand-blue)}
.content__footer .brand{left:16px;top:276px;font-size:6px;gap:3px}
.content__footer .brand__dot{width:5px;height:5px}
.page-no{position:absolute;right:15px;top:277px;width:10px;height:10px;border-radius:2px;background:var(--brand-blue);color:var(--white);font-size:5.5px;font-weight:700;display:flex;align-items:center;justify-content:center}

.toc{position:absolute;left:70px;top:93px;display:grid;grid-template-columns:213px 200px;row-gap:19px}
.toc__item{display:flex;align-items:flex-start;gap:8px}
.toc__num{width:20px;font-size:18px;font-weight:300;color:#b5b5b5;border-right:1px solid #d5d5d5;line-height:22px;padding-top:5px;text-align:left}
.toc__title{font-size:10.5px;font-weight:500;color:var(--accent-blue)}
.toc__text{font-size:5.4px;line-height:6.4px;color:var(--text-mid);margin-top:2px}

.columns{position:absolute;left:47px;top:89px;width:450px;display:grid;grid-template-columns:1fr 1fr;column-gap:22px}
.columns__head{font-size:10px;color:var(--accent-blue);margin-bottom:17px}
.columns p{font-size:6.2px;line-height:7.3px;color:var(--text-mid);margin-bottom:7px}
.bullets{list-style:none;font-size:6.2px;line-height:7.4px;color:var(--text-mid)}
.bullets>li{position:relative;padding-left:10px;margin-bottom:6px}
.bullets>li::before{content:"";position:absolute;left:0;top:3px;width:2.5px;height:2.5px;border-radius:50%;background:var(--brand-blue)}
.bullets ul{list-style:none;font-size:5.4px;line-height:7px}
.bullets ul li{position:relative;padding-left:10px;margin-left:10px}
.bullets ul li::before{content:"";position:absolute;left:0;top:3px;width:2px;height:2px;border-radius:50%;background:var(--accent-blue)}

.chart{position:absolute;left:40px;top:88px;width:250px;height:148px}
.legend{position:absolute;left:303px;top:88px;width:200px}
.legend__item{position:relative;height:38px;margin-bottom:16px;border:1px solid #d7d7d7;border-radius:5px;padding:7px 10px 0 18px;font-size:5.3px;line-height:6.4px;color:var(--text-mid)}
.legend__swatch{position:absolute;left:-6px;top:14px;width:9px;height:9px}

.data-table{position:absolute;left:28px;top:68px;width:484px;border-collapse:collapse;font-size:6.3px}
.data-table th{color:var(--white);font-weight:700;height:25px;font-size:6px;line-height:6.5px}
.data-table th:first-child{background:var(--brand-blue);text-align:left;padding-left:5px}
.data-table th.is-key{background:var(--accent-blue)}
.data-table th.is-other{background:var(--table-grey);border-left:1px solid #999}
.data-table td{height:21.8px;text-align:center;color:var(--text-mid);border-bottom:1px solid var(--rule)}
.data-table td:first-child{text-align:left;padding-left:5px;font-weight:500;color:var(--text-dark)}
.data-table td.is-key{color:var(--accent-blue);font-weight:700}
.data-table tr:nth-child(even) td{background:#f6f6f6}
.data-table col.label{width:150px}

/* back */
.back{background:#0f6cb4}
.back .brand{left:36px;top:65px;font-size:10.5px;color:var(--white)}
.contact{position:absolute;left:325px;top:171px}
.contact__title{font-size:10.5px;font-weight:500;color:var(--text-dark);margin-bottom:24px}
.contact__line{display:flex;align-items:center;gap:6px;font-size:6.8px;color:var(--text-mid);margin-bottom:6.5px}
.contact__line svg{width:9px;height:9px}
</style>
</head>
<body>

<!-- hero cover -->
<section class="slide slide--hero cover">
  <div class="cover__photo" role="img" aria-label="Photo of a city skyline and river bridge at dusk"></div>
  <div class="cover__fade"></div>
  <svg class="arcs" viewBox="0 0 540 303">
    <path d="M190,303 Q290,70 540,38 L540,58 Q320,92 232,303 Z" fill="var(--arc-grey)"/>
    <path d="M262,303 Q352,112 540,72 L540,98 Q385,138 300,303 Z" fill="var(--brand-blue)"/>
  </svg>
  <div class="cover__content">
    <div class="brand"><span class="brand__dot"></span>LANTERN-FOLK</div>
    <h1 class="cover__title">PRESENTATION<br>TITLE GOES HERE</h1>
    <p class="cover__lead">Lorem ipsum dolor sit amet, consectetur<br>adipiscing elit. Vivamus eu dui ex.</p>
    <p class="cover__date">Sunday, July 30, 2023</p>
    <p class="cover__copy">© 2023 Lantern-Folk, All Rights Reserved.</p>
  </div>
</section>

<!-- cover light -->
<section class="slide pos-a row-1 cover">
  <div class="cover__photo" role="img" aria-label="Photo of a city skyline and river bridge at dusk"></div>
  <div class="cover__fade"></div>
  <svg class="arcs" viewBox="0 0 540 303">
    <path d="M190,303 Q290,70 540,38 L540,58 Q320,92 232,303 Z" fill="var(--arc-grey)"/>
    <path d="M262,303 Q352,112 540,72 L540,98 Q385,138 300,303 Z" fill="var(--brand-blue)"/>
  </svg>
  <div class="cover__content">
    <div class="brand"><span class="brand__dot"></span>LANTERN-FOLK</div>
    <h1 class="cover__title">PRESENTATION<br>TITLE GOES HERE</h1>
    <p class="cover__lead">Lorem ipsum dolor sit amet, consectetur<br>adipiscing elit. Vivamus eu dui ex.</p>
    <p class="cover__date">Sunday, July 30, 2023</p>
    <p class="cover__copy">© 2023 Lantern-Folk, All Rights Reserved.</p>
  </div>
</section>

<!-- cover blue -->
<section class="slide pos-b row-1 cover cover--blue">
  <div class="cover__photo" role="img" aria-label="Photo of a city skyline and river bridge at dusk"></div>
  <div class="cover__fade cover__fade--blue"></div>
  <svg class="arcs" viewBox="0 0 540 303">
    <path d="M190,303 Q290,70 540,38 L540,58 Q320,92 232,303 Z" fill="var(--arc-grey)"/>
    <path d="M262,303 Q352,112 540,72 L540,98 Q385,138 300,303 Z" fill="var(--brand-blue)"/>
  </svg>
  <div class="cover__content">
    <div class="brand"><span class="brand__dot"></span>LANTERN-FOLK</div>
    <h1 class="cover__title">PRESENTATION<br>TITLE GOES HERE</h1>
    <p class="cover__lead">Lorem ipsum dolor sit amet, consectetur<br>adipiscing elit. Vivamus eu dui ex.</p>
    <p class="cover__date">Sunday, July 30, 2023</p>
    <p class="cover__copy">© 2023 Lantern-Folk, All Rights Reserved.</p>
  </div>
</section>

<!-- cover night -->
<section class="slide pos-a row-2 cover">
  <div class="cover__photo cover__photo--night" role="img" aria-label="Blue-toned photo of a city skyline and river bridge"></div>
  <div class="cover__fade"></div>
  <svg class="arcs" viewBox="0 0 540 303">
    <path d="M190,303 Q290,70 540,38 L540,58 Q320,92 232,303 Z" fill="var(--arc-grey)"/>
    <path d="M262,303 Q352,112 540,72 L540,98 Q385,138 300,303 Z" fill="var(--brand-blue)"/>
  </svg>
  <div class="cover__content">
    <div class="brand"><span class="brand__dot"></span>LANTERN-FOLK</div>
    <h1 class="cover__title">PRESENTATION<br>TITLE GOES HERE</h1>
    <p class="cover__lead">Lorem ipsum dolor sit amet, consectetur<br>adipiscing elit. Vivamus eu dui ex.</p>
    <p class="cover__date">Sunday, July 30, 2023</p>
    <p class="cover__copy">© 2023 Lantern-Folk, All Rights Reserved.</p>
  </div>
</section>

<!-- table of contents -->
<section class="slide pos-b row-2 content">
  <svg class="arcs" viewBox="0 0 540 303"><path d="M2,46 Q10,5 70,2" stroke="var(--arc-grey)" stroke-width="6" fill="none"/><path d="M4,62 Q16,11 82,6" stroke="var(--brand-blue)" stroke-width="6" fill="none"/></svg>
  <h2 class="content__heading">Heading Goes Here</h2>
  <div class="toc">
    <div class="toc__item"><span class="toc__num">1</span><div><div class="toc__title">Title Goes Here!</div><p class="toc__text">Lorem ipsum dolor sit amet, consectetur<br>adipiscing elit. Vivamus eu dui ex.</p></div></div>
    <div class="toc__item"><span class="toc__num">2</span><div><div class="toc__title">Title Goes Here!</div><p class="toc__text">Lorem ipsum dolor sit amet, consectetur<br>adipiscing elit. Vivamus eu dui ex.</p></div></div>
    <div class="toc__item"><span class="toc__num">3</span><div><div class="toc__title">Title Goes Here!</div><p class="toc__text">Lorem ipsum dolor sit amet, consectetur<br>adipiscing elit. Vivamus eu dui ex.</p></div></div>
    <div class="toc__item"><span class="toc__num">4</span><div><div class="toc__title">Title Goes Here!</div><p class="toc__text">Lorem ipsum dolor sit amet, consectetur<br>adipiscing elit. Vivamus eu dui ex.</p></div></div>
    <div class="toc__item"><span class="toc__num">5</span><div><div class="toc__title">Title Goes Here!</div><p class="toc__text">Lorem ipsum dolor sit amet, consectetur<br>adipiscing elit. Vivamus eu dui ex.</p></div></div>
    <div class="toc__item"><span class="toc__num">6</span><div><div class="toc__title">Title Goes Here!</div><p class="toc__text">Lorem ipsum dolor sit amet, consectetur<br>adipiscing elit. Vivamus eu dui ex.</p></div></div>
  </div>
  <div class="content__footer"><div class="brand"><span class="brand__dot"></span>LANTERN-FOLK</div></div>
  <span class="page-no">4</span>
</section>

<!-- two text columns -->
<section class="slide pos-a row-3 content">
  <svg class="arcs" viewBox="0 0 540 303"><path d="M2,46 Q10,5 70,2" stroke="var(--arc-grey)" stroke-width="6" fill="none"/><path d="M4,62 Q16,11 82,6" stroke="var(--brand-blue)" stroke-width="6" fill="none"/></svg>
  <h2 class="content__heading">Heading Goes Here</h2>
  <div class="columns">
    <div>
      <h3 class="columns__head">Heading Goes Here</h3>
      <p>Lorem ipsum dolor sit amet, consectetur adipiscing elit. Vivamus eu dui ex. Curabitur dapibus dignissim dui, in molestie metus feugiat sed. Praesent aliquet lorem ex, eu dapibus odio varius at. Duis eget tellus porta, consequat lacus vitae, venenatis dolor. Nulla facilisi. In et sollicitudin lacus.</p>
      <p>Nullam sit amet magna non ex bibendum mollis. Nunc vel neque eu augue dignissim congue ut vitae magna. Phasellus eget commodo arcu. Nunc vitae semper dui. Integer venenatis, tellus sit amet interdum pretium, erat neque rhoncus turpis, a aliquam augue ligula eget erat. Nunc placerat, arcu nec mattis fermentum, nisi mauris convallis nunc, ut luctus nunc nisl id ex.</p>
    </div>
    <div>
      <h3 class="columns__head">Heading Goes Here</h3>
      <p>Lorem ipsum dolor sit amet, consectetur adipiscing elit. Vivamus eu dui ex. Curabitur dapibus dignissim dui, in molestie metus feugiat sed. Praesent aliquet lorem ex, eu dapibus odio varius at. Duis eget tellus porta, consequat lacus vitae, venenatis dolor. Nulla facilisi. In et sollicitudin lacus.</p>
      <p>Nullam sit amet magna non ex bibendum mollis. Nunc vel neque eu augue dignissim congue ut vitae magna. Phasellus eget commodo arcu. Nunc vitae semper dui. Integer venenatis, tellus sit amet interdum pretium, erat neque rhoncus turpis, a aliquam augue ligula eget erat. Nunc placerat, arcu nec mattis fermentum, nisi mauris convallis nunc, ut luctus nunc nisl id ex.</p>
    </div>
  </div>
  <div class="content__footer"><div class="brand"><span class="brand__dot"></span>LANTERN-FOLK</div></div>
  <span class="page-no">5</span>
</section>

<!-- bullet columns -->
<section class="slide pos-b row-3 content">
  <svg class="arcs" viewBox="0 0 540 303"><path d="M2,46 Q10,5 70,2" stroke="var(--arc-grey)" stroke-width="6" fill="none"/><path d="M4,62 Q16,11 82,6" stroke="var(--brand-blue)" stroke-width="6" fill="none"/></svg>
  <h2 class="content__heading">Heading Goes Here</h2>
  <div class="columns">
    <div>
      <h3 class="columns__head" style="margin-bottom:12px">Heading Goes Here</h3>
      <ul class="bullets">
        <li>Lorem ipsum dolor sit amet, consectetur elit.<ul><li>Vivamus eu dui ex. Curabitur dapibus dignissim dui</li><li>consequat lacus vitae, venenatis dolor.</li></ul></li>
        <li>Nulla facilisi. In et sollicitudin lacus.<ul><li>Donec risus orci, gravida sit amet risus vehicula,</li><li>aliquet pretium sapien. Nullam sit amet magna non ex</li></ul></li>
        <li>bibendum mollis. Nunc vel neque eu augue dignissim<ul><li>congue ut vitae magna. Phasellus eget commodo arcu.</li><li>Nunc vitae semper dui. Integer venenatis, tellus sit</li></ul></li>
        <li>amet interdum pretium, erat neque rhoncus turpis<ul><li>a aliquam augue ligula eget erat.</li></ul></li>
      </ul>
    </div>
    <div>
      <h3 class="columns__head" style="margin-bottom:12px">Heading Goes Here</h3>
      <ul class="bullets">
        <li>Lorem ipsum dolor sit amet, consectetur elit.<ul><li>Vivamus eu dui ex. Curabitur dapibus dignissim dui</li><li>consequat lacus vitae, venenatis dolor.</li></ul></li>
        <li>Nulla facilisi. In et sollicitudin lacus.<ul><li>Donec risus orci, gravida sit amet risus vehicula,</li><li>aliquet pretium sapien. Nullam sit amet magna non ex</li></ul></li>
        <li>bibendum mollis. Nunc vel neque eu augue dignissim<ul><li>congue ut vitae magna. Phasellus eget commodo arcu.</li><li>Nunc vitae semper dui. Integer venenatis, tellus sit</li></ul></li>
        <li>amet interdum pretium, erat neque rhoncus turpis<ul><li>a aliquam augue ligula eget erat.</li></ul></li>
      </ul>
    </div>
  </div>
  <div class="content__footer"><div class="brand"><span class="brand__dot"></span>LANTERN-FOLK</div></div>
  <span class="page-no">6</span>
</section>

<!-- chart -->
<section class="slide pos-a row-4 content">
  <svg class="arcs" viewBox="0 0 540 303"><path d="M2,46 Q10,5 70,2" stroke="var(--arc-grey)" stroke-width="6" fill="none"/><path d="M4,62 Q16,11 82,6" stroke="var(--brand-blue)" stroke-width="6" fill="none"/></svg>
  <h2 class="content__heading">Heading Goes Here</h2>
  <svg class="arcs" viewBox="0 0 540 303" font-family="Roboto, sans-serif" font-size="4.5" fill="#666">
    <g stroke="#e6e6e6" stroke-width=".5">
      <line x1="55" x2="285" y1="224" y2="224"/><line x1="55" x2="285" y1="203" y2="203"/><line x1="55" x2="285" y1="182" y2="182"/><line x1="55" x2="285" y1="161" y2="161"/><line x1="55" x2="285" y1="140" y2="140"/><line x1="55" x2="285" y1="119" y2="119"/><line x1="55" x2="285" y1="98" y2="98"/>
    </g>
    <g text-anchor="end"><text x="50" y="226">0</text><text x="50" y="205">1</text><text x="50" y="184">2</text><text x="50" y="163">3</text><text x="50" y="142">4</text><text x="50" y="121">5</text><text x="50" y="100">6</text></g>
    <g fill="var(--brand-blue)"><rect x="64" y="133.7" width="6" height="90.3"/><rect x="101.5" y="171.5" width="6" height="52.5"/><rect x="139" y="150.5" width="6" height="73.5"/><rect x="176.5" y="129.5" width="6" height="94.5"/><rect x="214" y="133.7" width="6" height="90.3"/><rect x="251.5" y="171.5" width="6" height="52.5"/></g>
    <g fill="var(--accent-blue)"><rect x="72" y="173.6" width="6" height="50.4"/><rect x="109.5" y="131.6" width="6" height="92.4"/><rect x="147" y="186.2" width="6" height="37.8"/><rect x="184.5" y="165.2" width="6" height="58.8"/><rect x="222" y="173.6" width="6" height="50.4"/><rect x="259.5" y="131.6" width="6" height="92.4"/></g>
    <g fill="var(--table-grey)"><rect x="80" y="182" width="6" height="42"/><rect x="117.5" y="182" width="6" height="42"/><rect x="155" y="161" width="6" height="63"/><rect x="192.5" y="119" width="6" height="105"/><rect x="230" y="182" width="6" height="42"/><rect x="267.5" y="182" width="6" height="42"/></g>
    <g text-anchor="middle"><text x="75" y="233">Category 1</text><text x="112.5" y="233">Category 2</text><text x="150" y="233">Category 3</text><text x="187.5" y="233">Category 4</text><text x="225" y="233">Category 5</text><text x="262.5" y="233">Category 6</text></g>
  </svg>
  <div class="legend">
    <div class="legend__item"><span class="legend__swatch" style="background:var(--brand-blue)"></span>Lorem ipsum dolor sit amet, at laborum nibh duis mauris. Per ultrices lectus sed metus tristique eu. Diam suspendisse ac ipsum maecenas fermentum.</div>
    <div class="legend__item"><span class="legend__swatch" style="background:var(--accent-blue)"></span>Lorem ipsum dolor sit amet, at laborum nibh duis mauris. Per ultrices lectus sed metus tristique eu. Diam suspendisse ac ipsum maecenas fermentum.</div>
    <div class="legend__item"><span class="legend__swatch" style="background:var(--table-grey)"></span>Lorem ipsum dolor sit amet, at laborum nibh duis mauris. Per ultrices lectus sed metus tristique eu. Diam suspendisse ac ipsum maecenas fermentum.</div>
  </div>
  <div class="content__footer"><div class="brand"><span class="brand__dot"></span>LANTERN-FOLK</div></div>
  <span class="page-no">7</span>
</section>

<!-- table -->
<section class="slide pos-b row-4 content">
  <svg class="arcs" viewBox="0 0 540 303"><path d="M2,46 Q10,5 70,2" stroke="var(--arc-grey)" stroke-width="6" fill="none"/><path d="M4,62 Q16,11 82,6" stroke="var(--brand-blue)" stroke-width="6" fill="none"/></svg>
  <h2 class="content__heading">Heading Goes Here</h2>
  <table class="data-table">
    <colgroup><col class="label"><col><col><col><col></colgroup>
    <thead><tr><th>Heading Goes Here</th><th class="is-key">Heading<br>Goes Here</th><th class="is-other">Heading<br>Goes Here</th><th class="is-other">Heading<br>Goes Here</th><th class="is-other">Heading<br>Goes Here</th></tr></thead>
    <tbody>
      <tr><td>Lorem ipsum dolor sit amet</td><td class="is-key">23</td><td>12</td><td>78</td><td>78</td></tr>
      <tr><td>Vivamus eu dui ex. Curabitur dapibus</td><td class="is-key">45</td><td>56</td><td>12</td><td>76</td></tr>
      <tr><td>Praesent aliquet lorem ex, eu dapibus</td><td class="is-key">78</td><td>76</td><td>34</td><td>34</td></tr>
      <tr><td>Duis eget tellus porta, consequat lacus</td><td class="is-key">22</td><td>12</td><td>55</td><td>67</td></tr>
      <tr><td>Donec risus orci, gravida sit amet</td><td class="is-key">34</td><td>66</td><td>45</td><td>11</td></tr>
      <tr><td>Nunc placerat, arcu nec mattis</td><td class="is-key">67</td><td>47</td><td>78</td><td>23</td></tr>
      <tr><td>Nam semper tristique mauris</td><td class="is-key">87</td><td>67</td><td>12</td><td>45</td></tr>
    </tbody>
  </table>
  <div class="content__footer"><div class="brand"><span class="brand__dot"></span>LANTERN-FOLK</div></div>
  <span class="page-no">8</span>
</section>

<!-- back page -->
<section class="slide slide--back back">
  <svg class="arcs" viewBox="0 0 540 303">
    <path d="M60,303 Q160,80 540,15 L540,303 Z" fill="#1b4f86" role="img" aria-label="Blue-toned photo of a city skyline at dusk"/>
    <path d="M84,303 Q200,60 540,8 L540,28 Q232,82 125,303 Z" fill="var(--arc-grey)"/>
    <path d="M138,303 Q245,95 540,36 L540,56 Q272,115 175,303 Z" fill="var(--brand-blue)"/>
    <path d="M190,303 Q285,125 540,64 L540,303 Z" fill="var(--white)"/>
  </svg>
  <div class="brand"><span class="brand__dot"></span>LANTERN-FOLK</div>
  <div class="contact">
    <h2 class="contact__title">CONTACT US</h2>
    <p class="contact__line"><svg viewBox="0 0 10 10"><path d="M2.4 1.2 L3.8 2.9 L3 3.9 Q4 5.9 6 7 L7 6.2 L8.7 7.6 L7.6 8.9 Q3.8 8.6 1.1 2.3 Z" fill="none" stroke="var(--brand-blue)" stroke-width=".9" stroke-linejoin="round"/></svg>Phone Number Goes Here</p>
    <p class="contact__line"><svg viewBox="0 0 10 10"><circle cx="5" cy="5" r="1.8" fill="none" stroke="var(--brand-blue)" stroke-width=".9"/><path d="M6.8 5 V6 Q6.8 7.2 7.8 7.2 Q9 7.2 9 5 A4 4 0 1 0 7 8.5" fill="none" stroke="var(--brand-blue)" stroke-width=".9"/></svg>E-Mail Address Goes Here</p>
    <p class="contact__line"><svg viewBox="0 0 10 10"><g fill="none" stroke="var(--brand-blue)" stroke-width=".8"><circle cx="5" cy="5" r="4"/><ellipse cx="5" cy="5" rx="1.8" ry="4"/><line x1="1" y1="5" x2="9" y2="5"/></g></svg>URL Address Goes Here</p>
  </div>
</section>

</body>
</html>
```